Bruntel general construction

We need an website that are similar to these websites:
https://www.morvexa.com/en/
https://dulnari.com/company/

but with a tweak. Do not copy the entire website but atleast similar and yet better than them.

For reference this our current website.
https://bruntel.ph/

For the winning Designer please help us with the migration from our old website to the new redesign website.

```html
<!DOCTYPE html>
<html lang="en">
<head>
<meta charset="utf-8">
<title>Bruntel — Integrated Industrial Services</title>
<link rel="stylesheet" href="https://fonts.googleapis.com/css2?family=Inter+Tight:wght@400;500;600;700&display=swap">
<style>
:root{
  --navy:#0b1a33;
  --navy-deep:#081429;
  --navy-mid:#13305a;
  --orange:#f26b1d;
  --orange-soft:#ff8a3d;
  --paper:#f2f5f9;
  --ink:#0d1c36;
  --muted:#5b6b82;
  --line:#d5dce6;
  --line-dark:rgba(255,255,255,.12);
  --tag:#2f7fbf;
  --white:#ffffff;
}
*{margin:0;padding:0;box-sizing:border-box}
html,body{width:1200px;height:3606px;overflow:hidden}
body{font-family:"Inter Tight",Helvetica,Arial,sans-serif;color:var(--ink);background:var(--paper);position:relative}
.eyebrow{position:absolute;font-size:7px;letter-spacing:.22em;font-weight:600;text-transform:uppercase;color:var(--orange);display:flex;align-items:center;gap:10px;white-space:nowrap}
.eyebrow::before{content:"";width:24px;height:1.5px;background:currentColor}
.side-label{position:absolute;font-size:6.5px;letter-spacing:.2em;text-transform:uppercase;color:var(--muted);white-space:nowrap}
.side-label b{color:var(--orange);font-weight:600;margin-right:10px}
.hl{color:var(--orange)}
h1,h2{font-weight:500;letter-spacing:-.035em;line-height:1.08}

/* nav */
.site-nav{position:absolute;top:0;left:0;width:1200px;height:56px;background:var(--navy-deep);border-bottom:1px solid var(--line-dark);z-index:5}
.brand{position:absolute;display:flex;align-items:center;gap:6px;color:var(--orange);font-weight:600;letter-spacing:.06em;font-size:11px}
.brand i{width:9px;height:9px;border-radius:50%;background:var(--orange)}
.nav-links{position:absolute;top:23px;left:749px;display:flex;gap:27px;font-size:7.5px;letter-spacing:.12em;color:#c8d2e2;white-space:nowrap}
.nav-cta{position:absolute;left:1039px;top:13px;width:112px;height:29px;background:#ffa11a;color:var(--navy);font-size:7.5px;font-weight:700;letter-spacing:.1em;display:flex;align-items:center;padding-left:12px;white-space:nowrap}
.nav-cta span{position:absolute;right:12px}

/* hero */
.hero{position:absolute;top:56px;left:0;width:1200px;height:427px;background:var(--navy)}
.hero-photo{position:absolute;left:602px;top:0;width:598px;height:427px;background:linear-gradient(160deg,#1f4f93 0%,#153a74 40%,#0c2048 100%)}
.hero-fade{position:absolute;left:0;top:0;width:760px;height:427px;background:linear-gradient(90deg,var(--navy) 75%,rgba(11,26,51,0))}
.hero-strip{position:absolute;left:1108px;top:0;width:92px;height:427px;background:#060f20}
.hero-strip span{position:absolute;left:60px;top:28px;writing-mode:vertical-rl;font-size:6.5px;letter-spacing:.25em;color:#9fb0c8}
.hero h1{position:absolute;left:66px;top:118px;font-size:56px;color:var(--white);line-height:.97;white-space:nowrap}
.hero p{position:absolute;left:66px;top:250px;width:400px;font-size:12px;line-height:1.6;color:#dbe3ef}
.btn{position:absolute;height:33px;background:var(--orange);color:var(--white);font-size:7px;font-weight:700;letter-spacing:.14em;display:flex;align-items:center;padding-left:14px;box-shadow:0 8px 18px rgba(242,107,29,.35);white-space:nowrap}
.btn span{position:absolute;right:14px}
.link-btn{position:absolute;font-size:7px;letter-spacing:.14em;color:#dbe3ef;border-bottom:1px solid #6a7a93;padding-bottom:10px;width:124px;white-space:nowrap}
.link-btn span{color:var(--orange);margin-left:8px}
.hero-card{position:absolute;left:928px;top:295px;width:223px;height:108px;background:rgba(11,26,51,.92);border-left:2px solid var(--orange);padding:22px 20px}
.hero-card small{display:block;font-size:5.5px;letter-spacing:.2em;color:var(--orange);font-weight:600}
.hero-card strong{display:block;margin-top:10px;font-size:12px;line-height:1.35;color:var(--white);font-weight:600}
.hero-card em{display:block;margin-top:8px;font-style:normal;font-size:6px;color:#9fb0c8}

.stats{position:absolute;top:483px;left:0;width:1200px;height:80px;background:var(--navy-deep);border-top:1px solid var(--line-dark);display:flex}
.stat{width:300px;border-right:1px solid var(--line-dark);display:flex;align-items:center;padding-left:24px;gap:12px;color:var(--white)}
.stat:last-child{border-right:0}
.stat.first{padding-left:65px;display:block;padding-top:22px}
.stat.first strong{font-size:13px;font-weight:600;display:block}
.stat.first small{font-size:7px;color:#9fb0c8}
.badge{width:28px;height:28px;border-radius:50%;border:1px solid #566783}
.stat b{font-size:7px;font-weight:600;display:block}
.stat em{font-style:normal;font-size:6px;letter-spacing:.12em;color:#8596b0}

/* who */
.who{position:absolute;top:563px;left:0;width:1200px;height:417px;background:var(--paper)}
.who h2{position:absolute;left:283px;top:114px;font-size:44px;white-space:nowrap}
.who .rule{position:absolute;left:283px;top:206px;width:686px;height:1px;background:var(--line)}
.who .lead{position:absolute;left:283px;top:226px;width:350px;font-size:16px;line-height:1.52}
.who .body{position:absolute;left:711px;top:229px;width:256px;font-size:9.5px;line-height:1.78;color:#44546c}
.who .more{position:absolute;left:711px;top:312px;font-size:6px;letter-spacing:.18em;color:var(--orange);font-weight:600;border-bottom:1px solid #c7cfdb;padding-bottom:7px;width:114px;white-space:nowrap}

/* sectors */
.sectors{position:absolute;top:980px;left:0;width:1200px;height:1017px;background:var(--navy)}
.sectors h2{position:absolute;left:301px;top:106px;font-size:44px;color:var(--white);line-height:1.03}
.sectors .intro{position:absolute;left:813px;top:170px;width:290px;font-size:9px;line-height:1.75;color:#c6d1e1}
.card{position:absolute;background:var(--white);height:345px}
.card .photo{height:146px;background:linear-gradient(180deg,#4a5b77 0%,#3d5675 55%,#2b4466 100%)}
.card .num{position:absolute;left:20px;top:175px;font-size:6.5px;color:var(--orange);font-weight:600}
.card h3{position:absolute;left:52px;top:170px;font-size:17px;font-weight:500;letter-spacing:-.02em}
.card p{position:absolute;left:52px;top:206px;right:40px;font-size:9.5px;line-height:1.7;color:#44546c}
.card .rule{position:absolute;left:52px;right:20px;bottom:39px;height:1px;background:#e3e8ef}
.card .tags{position:absolute;left:52px;bottom:19px;display:flex;gap:12px;font-size:5.5px;letter-spacing:.14em;font-weight:700;color:var(--tag);white-space:nowrap}

/* approach */
.approach{position:absolute;top:1997px;left:0;width:1200px;height:628px;background:var(--paper)}
.approach h2{position:absolute;left:311px;top:117px;font-size:44px;line-height:1.1}
.steps{position:absolute;left:311px;top:293px;width:469px;border-top:1px solid var(--line);list-style:none}
.steps li{height:40.6px;border-bottom:1px solid var(--line);display:flex;align-items:center;font-size:9px;font-weight:600}
.steps li i{font-style:normal;font-size:5.5px;color:#8a97a9;width:34px;font-weight:500}
.steps li span{margin-left:auto;color:var(--orange);font-size:11px;font-weight:400}
.safety{position:absolute;left:832px;top:226px;width:298px;height:312px;background:var(--navy)}
.safety .photo{height:168px;background:linear-gradient(180deg,#5f7fa8 0%,#4c6b94 60%,#2d4a73 100%)}
.safety small{position:absolute;left:20px;top:196px;font-size:5.5px;letter-spacing:.16em;color:var(--orange);font-weight:600}
.safety h4{position:absolute;left:20px;top:214px;width:260px;font-size:16px;font-weight:500;color:var(--white);line-height:1.2;letter-spacing:-.02em}
.safety p{position:absolute;left:20px;top:268px;width:262px;font-size:8px;line-height:1.7;color:#c6d1e1}

/* promise */
.promise{position:absolute;top:2625px;left:0;width:1200px;height:339px;background:linear-gradient(110deg,#163563 0%,#12305a 55%,#0f284c 100%)}
.promise .eyebrow{color:#4f9ad6}
.promise blockquote{position:absolute;left:119px;top:118px;font-size:41px;letter-spacing:-.035em;line-height:1.15;color:var(--white);white-space:nowrap}
.promise .rule{position:absolute;left:119px;top:239px;width:963px;height:1px;background:var(--line-dark)}
.values{position:absolute;left:119px;top:257px;display:flex;gap:34px;font-size:5.5px;letter-spacing:.14em;color:#b9c6da;white-space:nowrap}
.values span::before{content:"";display:inline-block;width:3px;height:3px;border-radius:50%;background:var(--orange);margin-right:7px;vertical-align:middle}

/* contact */
.contact{position:absolute;top:2964px;left:0;width:1200px;height:407px;background:var(--white)}
.contact h2{position:absolute;left:81px;top:126px;font-size:47px;line-height:1.05;white-space:nowrap}
.contact p{position:absolute;left:81px;top:234px;width:340px;font-size:8.5px;line-height:1.75;color:#44546c}
.offices{position:absolute;left:720px;top:152px;width:400px;border-top:1px solid var(--line)}
.office{height:81px;border-bottom:1px solid var(--line);position:relative}
.office small{position:absolute;left:0;top:20px;font-size:5px;letter-spacing:.15em;color:var(--orange)}
.office strong{position:absolute;left:69px;top:20px;font-size:9px;font-weight:600;line-height:1.5;white-space:nowrap}
.office em{position:absolute;left:69px;top:50px;font-style:normal;font-size:6.5px;color:#5b6b82}

/* footer */
.site-footer{position:absolute;top:3371px;left:0;width:1200px;height:235px;background:var(--navy-deep);color:#b9c6da}
.site-footer .tag{position:absolute;right:60px;top:72px;font-size:7px}
.site-footer .rule{position:absolute;left:60px;right:60px;height:1px;background:var(--line-dark)}
.foot-links{position:absolute;left:60px;top:144px;display:flex;gap:22px;font-size:6.5px;letter-spacing:.12em}
.site-footer .copy{position:absolute;left:60px;top:212px;font-size:5.5px;letter-spacing:.1em;color:#7d8da6}
.site-footer .top{position:absolute;right:60px;top:212px;font-size:5.5px;letter-spacing:.12em}
</style>
</head>
<body>

<header class="site-nav">
  <div class="brand" style="left:63px;top:21px"><i></i>BRUNTEL</div>
  <nav class="nav-links"><span>COMPANY</span><span>SERVICES</span><span>OUR APPROACH</span><span>CONTACT</span></nav>
  <a class="nav-cta">START A PROJECT<span>↗</span></a>
</header>

<section class="hero">
  <div class="hero-photo" role="img" aria-label="Industrial plant with pipework and towers lit at dusk in deep blue tones"></div>
  <div class="hero-fade"></div>
  <div class="hero-strip"><span>PHILIPPINES / ASIA</span></div>
  <div class="eyebrow" style="left:66px;top:91px;color:#4f9ad6">ENGINEERING CONTINUITY</div>
  <h1>Built for the systems that<br>keep <span class="hl">industries moving.</span></h1>
  <p>From complex construction to critical maintenance, we keep industrial assets safe, reliable and ready for what comes next.</p>
  <a class="btn" style="left:66px;top:316px;width:130px">START A PROJECT<span>↗</span></a>
  <a class="link-btn" style="left:214px;top:327px">EXPLORE OUR CAPABILITIES<span>↓</span></a>
  <div class="hero-card">
    <small>ONE INTEGRATED PARTNER</small>
    <strong>Engineering. Construction.<br>Maintenance.</strong>
    <em>Delivered with safety at the centre.</em>
  </div>
</section>

<div class="stats">
  <div class="stat first"><strong>One partner.</strong><small>From project delivery to long-term performance.</small></div>
  <div class="stat"><div class="badge"></div><div><b>Regional support</b><em>MULTI-SECTOR DELIVERY</em></div></div>
  <div class="stat"><div class="badge"></div><div><b>ISO 9001</b><em>QUALITY MANAGEMENT</em></div></div>
  <div class="stat"><div class="badge"></div><div><b>Accredited</b><em>LICENSED CONTRACTOR</em></div></div>
</div>

<section class="who">
  <div class="eyebrow" style="left:283px;top:91px">WHO WE ARE</div>
  <h2>Industrial services, <span class="hl">from one source.</span></h2>
  <div class="side-label" style="left:70px;top:204px"><b>01</b>COMPANY</div>
  <div class="rule"></div>
  <p class="lead">Bruntel supports the oil, gas, power, water and environmental industries with integrated expertise across the full asset lifecycle.</p>
  <p class="body">Our model brings construction, maintenance, specialist manpower and environmental capability together—reducing complexity, protecting schedules and helping clients operate with confidence.</p>
  <a class="more">DISCOVER OUR APPROACH <span style="margin-left:12px">↗</span></a>
</section>

<section class="sectors">
  <div class="eyebrow" style="left:301px;top:84px;color:#4f9ad6">WHAT WE DO</div>
  <h2>Five sectors.<br><span class="hl">One standard.</span></h2>
  <div class="side-label" style="left:49px;top:192px;color:#8596b0"><b>02</b>MARKET EXPERTISE</div>
  <p class="intro">Practical capability for essential industrial systems, delivered with safety, accountability and respect for the environment.</p>

  <article class="card" style="left:49px;top:239px;width:546px">
    <div class="photo" role="img" aria-label="Wind turbine before mountains under a cloudy evening sky"></div>
    <span class="num">01</span><h3>Environment</h3>
    <p>Waste-to-energy infrastructure for municipal, industrial and biodegradable waste streams.</p>
    <div class="rule"></div><div class="tags"><span>WASTE TO ENERGY</span><span>RESOURCE RECOVERY</span></div>
  </article>
  <article class="card" style="left:603px;top:239px;width:548px">
    <div class="photo" role="img" aria-label="Refinery skyline with tanks and flare stacks at dusk"></div>
    <span class="num">02</span><h3>Oil &amp; Gas</h3>
    <p>Fabric maintenance and multi-skilled support for offshore, onshore and downstream assets.</p>
    <div class="rule"></div><div class="tags"><span>OFFSHORE</span><span>DOWNSTREAM</span></div>
  </article>
  <article class="card" style="left:49px;top:592px;width:361px">
    <div class="photo" role="img" aria-label="Water treatment basins beside a city skyline"></div>
    <span class="num">03</span><h3>Water</h3>
    <p>Construction and maintenance for desalination, sewage treatment and water systems.</p>
    <div class="rule"></div><div class="tags"><span>DESALINATION</span><span>WATER TREATMENT</span></div>
  </article>
  <article class="card" style="left:419px;top:592px;width:361px">
    <div class="photo" role="img" aria-label="Power generation plant with storage tanks"></div>
    <span class="num">04</span><h3>Power</h3>
    <p>Boiler construction, plant maintenance and life-extension support for power generation.</p>
    <div class="rule"></div><div class="tags"><span>BOILERS</span><span>PLANT MAINTENANCE</span></div>
  </article>
  <article class="card" style="left:790px;top:592px;width:361px">
    <div class="photo" role="img" aria-label="Tower crane over a steel frame construction site"></div>
    <span class="num">05</span><h3>Construction</h3>
    <p>End-to-end construction, repair and manpower solutions delivered to exacting standards.</p>
    <div class="rule"></div><div class="tags"><span>NEW BUILD</span><span>REPAIR &amp; MAINTENANCE</span></div>
  </article>
</section>

<section class="approach">
  <div class="eyebrow" style="left:311px;top:92px">HOW WE WORK</div>
  <h2>Where reliability<br>becomes a <span class="hl">working<br>system.</span></h2>
  <div class="side-label" style="left:70px;top:314px"><b>03</b>LIFECYCLE DELIVERY</div>
  <ol class="steps">
    <li><i>01</i>New construction<span>→</span></li>
    <li><i>02</i>Repair &amp; maintenance<span>→</span></li>
    <li><i>03</i>Plant shutdowns<span>→</span></li>
    <li><i>04</i>Asset modifications<span>→</span></li>
    <li><i>05</i>Decommissioning<span>→</span></li>
    <li><i>06</i>Recruitment &amp; manpower<span>→</span></li>
  </ol>
  <aside class="safety">
    <div class="photo" role="img" aria-label="Tower crane and steel structure against a blue sky"></div>
    <small>HSE / EVERY PROJECT</small>
    <h4>Safety is not a statistic. It is how we work.</h4>
    <p>We protect our people, our clients, surrounding communities and the environment through disciplined execution.</p>
  </aside>
</section>

<section class="promise">
  <div class="eyebrow" style="left:119px;top:76px">THE BRUNTEL PROMISE</div>
  <blockquote>“We deliver what we promise—and work<br>to exceed what our clients expect.”</blockquote>
  <div class="rule"></div>
  <div class="values"><span>QUALITY-LED</span><span>SAFETY-FOCUSED</span><span>ENVIRONMENTALLY RESPONSIBLE</span></div>
</section>

<section class="contact">
  <div class="eyebrow" style="left:81px;top:91px">START A CONVERSATION</div>
  <h2>What needs to keep<br><span class="hl">moving?</span></h2>
  <p>Tell us about your site, asset or next project. Our team will connect you with the right expertise.</p>
  <a class="btn" style="left:81px;top:283px;width:132px">INFO@BRUNTEL.PH<span>↗</span></a>
  <div class="offices">
    <div class="office"><small>CALDERON</small><strong>Calderon City<br>Philippines 4190</strong><em>+63 (0) 43 555-0142</em></div>
    <div class="office"><small>VERANO</small><strong>Lumara City, Verano<br>Philippines 4120</strong><em>+63 (0) 46 555-0178</em></div>
  </div>
</section>

<footer class="site-footer">
  <div class="brand" style="left:74px;top:66px"><i></i>BRUNTEL</div>
  <div class="tag">Integrated industrial services across the Philippines and Asia.</div>
  <div class="rule" style="top:123px"></div>
  <nav class="foot-links"><span>COMPANY</span><span>SERVICES</span><span>APPROACH</span><span>CONTACT</span></nav>
  <div class="rule" style="top:192px"></div>
  <div class="copy">© 2026 BRUNTEL. ALL RIGHTS RESERVED</div>
  <div class="top">BACK TO TOP ↑</div>
</footer>

</body>
</html>
```